Selka Varon Photography

I need a website design for my photography business, I want something clean, elegant, Classy.. I like the colors, White, Black, Green/Blue, Pink, Brown, Lavender,, I have a lot added my Logo .... Additional Info... I need a Photography Website Design, with probably 6 Tabs, Home, About Me, Portfolio, Gallery, Investment, Contact.
Home Page should have my logo, Name & Address, Social Media Icons, and Pictures.
As long as the templates are made I have a hosting coming that will code it.
Portraits Photography, Senior Portraits, Newborn, Families, Events, Engagements, Wedding,
Business
5+ page

```html
<!DOCTYPE html>
<html lang="en">
<head>
<meta charset="utf-8">
<title>Selka Varon Photography</title>
<link href="https://fonts.googleapis.com/css2?family=Raleway:wght@300;400;500&family=Open+Sans:ital,wght@0,400;0,600;1,700&display=swap" rel="stylesheet">
<style>
:root{
  --ink:#2b2b2d;
  --charcoal:#262628;
  --band:#1f1f1f;
  --teal:#0f6e63;
  --teal-bright:#1fc7c0;
  --teal-title:#7ce6df;
  --pink:#eaa4c8;
  --pink-ink:#4a3640;
  --white:#ffffff;
  --muted:#d0d0d0;
  --footer:#3a3a36;
  --footer-ink:#a8a8a0;
}
*{box-sizing:border-box;margin:0;padding:0}
html,body{width:831px;height:1200px;overflow:hidden;background:var(--white)}
body{font-family:"Open Sans",Arial,sans-serif;color:var(--ink)}
.page{position:relative;width:831px;height:1200px;overflow:hidden}
.abs{position:absolute}

/* top bar */
.topbar{left:0;top:0;width:831px;height:21px;background:#56607e;color:var(--white);font-size:6.5px}
.topbar .contact-info{position:absolute;left:168px;top:0;height:21px;display:flex;gap:6px;align-items:center}
.topbar .socials{position:absolute;left:602px;top:0;height:21px;display:flex;gap:6px;align-items:center}
.social-chip{display:block;width:7px;height:7px;border:1px solid rgba(255,255,255,.9);border-radius:2px}

/* hero */
.hero{left:0;top:21px;width:831px;height:392px;
  background:linear-gradient(180deg,#7d8cb4 0%,#c9a58a 14%,#e5b07a 24%,#8a5f76 32%,#6e5468 38%,#7f8a60 46%,#c3b46a 54%,#7c9a78 62%,#4d9790 72%,#2f8a8a 82%,#8a5a3a 92%,#c2592c 100%)}
.brand{left:160px;top:40px;width:150px;text-align:center;color:var(--ink);font-family:"Raleway",sans-serif;font-weight:400}
.brand .mark{width:28px;height:28px;border-radius:50%;background:var(--ink);margin:0 auto 3px}
.brand .name{font-size:24px;line-height:1;white-space:nowrap}
.brand .sub{font-size:7.5px;letter-spacing:3px;margin-top:3px;white-space:nowrap}
.nav{left:411px;top:76px;display:flex;gap:2px;font-size:7px;color:var(--band)}
.nav a{color:inherit;text-decoration:none;padding:5px 8px;border-radius:3px}
.nav a.active{background:#4a4a48;color:var(--white)}
.hero-band{left:0;top:178px;width:831px;height:78px;background:rgba(40,40,50,.32)}
.hero-title{left:0;top:190px;width:831px;text-align:center;color:var(--white);font-family:"Raleway",sans-serif;font-weight:300;font-size:40px;letter-spacing:1px;line-height:50px}
.arrow{top:199px}

/* about */
.about{left:0;top:416px;width:831px;height:166px;background:var(--charcoal)}
.avatar{left:186px;top:446px;width:108px;height:108px;border-radius:50%;border:3px solid var(--white);background:linear-gradient(160deg,#3f5a2e,#b9917e 45%,#6b4e38 80%)}
.about-name{left:345px;top:437px;color:var(--white);font-family:"Raleway",sans-serif;font-weight:300;font-size:27px;line-height:34px;white-space:nowrap}
.about-role{left:345px;top:468px;color:var(--teal-bright);font-style:italic;font-weight:700;font-size:7.5px}
.about-text{left:345px;top:487px;width:312px;color:var(--muted);font-size:7px;line-height:10.4px}
.btn-pink{background:var(--pink);color:var(--pink-ink);font-family:"Raleway",sans-serif;display:flex;align-items:center;justify-content:center}
.read-more{left:346px;top:541px;width:99px;height:22px;font-size:8px}

/* portfolio */
.portfolio-band{left:0;top:582px;width:831px;height:45px;background:var(--teal);border-top:1px solid #5fb3a8}
.portfolio-title{left:0;top:587px;width:831px;text-align:center;color:var(--teal-title);font-family:"Raleway",sans-serif;font-weight:400;font-size:26px;line-height:34px}
.tile{display:flex;align-items:center;justify-content:center;color:var(--white);font-family:"Raleway",sans-serif;font-weight:400;font-size:12.5px;white-space:nowrap}
.t1{left:0;top:627px;width:260px;height:190px;background:linear-gradient(180deg,#6a6866,#54524f 50%,#3a3937)}
.t2{left:260px;top:627px;width:285px;height:190px;background:linear-gradient(180deg,#4d5a34,#8f7462 45%,#5a4636 80%,#6e6450)}
.t3{left:545px;top:627px;width:286px;height:190px;background:linear-gradient(180deg,#2e3a2c,#3c4438 55%,#1f3c3e)}
.t4{left:0;top:817px;width:260px;height:191px;background:linear-gradient(180deg,#5a5a56,#3e3d3b 60%,#2a2928)}
.t5{left:260px;top:817px;width:285px;height:191px;background:linear-gradient(180deg,#2a2520,#3e332a 55%,#231f1a)}
.t6{left:545px;top:817px;width:286px;height:191px;background:linear-gradient(180deg,#5e4a3e,#6e5446 50%,#3e3430)}

/* contact band */
.contact-band{left:0;top:1008px;width:831px;height:54px;background:var(--band)}
.contact-line{left:184px;top:1026px;color:var(--white);font-family:"Raleway",sans-serif;font-size:13px;white-space:nowrap}
.contact-line small{font-family:"Open Sans",sans-serif;font-size:6.5px}
.contact-btn{left:525px;top:1023px;width:124px;height:25px;font-size:10px}

/* follow */
.follow-text{left:0;top:1077px;width:831px;text-align:center;font-size:7px;color:#444}
.follow-btn{left:353px;top:1102px;width:125px;height:25px;border:1px solid var(--band);color:var(--ink);display:flex;align-items:center;justify-content:center;font-family:"Raleway",sans-serif;font-size:10px;letter-spacing:.5px}
.follow-icons{left:0;top:1137px;width:831px;display:flex;justify-content:center;gap:11px}
.follow-icons .social-chip{width:9px;height:9px;border:1.5px solid var(--band)}

/* footer */
.footer{left:0;top:1164px;width:831px;height:36px;background:var(--footer);color:var(--footer-ink);font-size:6px;display:flex;align-items:center;justify-content:center}
</style>
</head>
<body>
<div class="page">
  <div class="abs topbar">
    <div class="contact-info">
      <svg width="6" height="6" viewBox="0 0 10 10"><path d="M2 1l2 2-1 1.5a6 6 0 0 0 2.5 2.5L7 6l2 2-1.5 1.5C4 9 1 6 .5 2.5z" fill="#fff"/></svg>
      <span>555.0142.7788</span><span>|</span>
      <svg width="7" height="5" viewBox="0 0 14 10"><rect x=".5" y=".5" width="13" height="9" fill="none" stroke="#fff"/><path d="M.5 .5l6.5 5 6.5-5" fill="none" stroke="#fff"/></svg>
      <span>info@selkavaronphoto.com</span>
    </div>
    <div class="socials" aria-label="Social media links"><span class="social-chip"></span><span class="social-chip"></span><span class="social-chip"></span><span class="social-chip"></span><span class="social-chip"></span></div>
  </div>

  <div class="abs hero" role="img" aria-label="Mountain lake at sunset with three wooden rowboats in the foreground"></div>
  <div class="abs brand">
    <div class="mark"></div>
    <div class="name">Selka Varon</div>
    <div class="sub">PHOTOGRAPHY</div>
  </div>
  <nav class="abs nav">
    <a class="active" href="#">Home</a><a href="#">About Me</a><a href="#">Portfolio</a><a href="#">Gallery</a><a href="#">Investment</a><a href="#">Contact</a>
  </nav>
  <div class="abs hero-band"></div>
  <h1 class="abs hero-title">EXCELLENT SOLUTION</h1>
  <svg class="abs arrow" style="left:91px" width="34" height="34" viewBox="0 0 34 34"><circle cx="17" cy="17" r="16" fill="none" stroke="#fff" stroke-width="1.5"/><path d="M20 9l-8 8 8 8" fill="none" stroke="#fff" stroke-width="1.5"/></svg>
  <svg class="abs arrow" style="left:693px" width="34" height="34" viewBox="0 0 34 34"><circle cx="17" cy="17" r="16" fill="none" stroke="rgba(255,255,255,.6)" stroke-width="1.5"/><path d="M14 9l8 8-8 8" fill="none" stroke="rgba(255,255,255,.6)" stroke-width="1.5"/></svg>

  <section class="abs about"></section>
  <div class="abs avatar" role="img" aria-label="Portrait of the photographer in a plaid cap"></div>
  <h2 class="abs about-name">SELKA VARON</h2>
  <p class="abs about-role">WEDDING, PORTRAIT, LANDSCAPE PHOTOGRAHER</p>
  <p class="abs about-text">Lorem ipsum dolor sit amet, consectetur adipiscing elit. Fusce eget sagittis magna. Sed condimentum semper diam, dignissim auctor enim varius eu. Nunc non nisl eu mauris maximus sagittis. Curabitur eget purus lacinia, consequat sapien sit amet, dignissim odio. Sed sit amet malesuada orci. Vestibulum placerat turpis ut diam viverra convallis.</p>
  <a class="abs btn-pink read-more">READ MORE</a>

  <div class="abs portfolio-band"></div>
  <h2 class="abs portfolio-title">PORTFOLIO</h2>
  <div class="abs tile t1" role="img" aria-label="Black and white close-up portrait of a toddler">SAMPLE IMAGE - CATEGORY 1</div>
  <div class="abs tile t2" role="img" aria-label="Outdoor portrait of a young woman in a plaid cap">SAMPLE IMAGE - CATEGORY 1</div>
  <div class="abs tile t3" role="img" aria-label="Woman lying on the hood of a vintage car under palm trees">SAMPLE IMAGE - CATEGORY 1</div>
  <div class="abs tile t4" role="img" aria-label="Black and white portrait of a woman holding a hat brim">SAMPLE IMAGE - CATEGORY 1</div>
  <div class="abs tile t5" role="img" aria-label="Newborn baby in a knitted flower headband">SAMPLE IMAGE - CATEGORY 1</div>
  <div class="abs tile t6" role="img" aria-label="Close portrait of a young woman with long hair">SAMPLE IMAGE - CATEGORY 1</div>

  <div class="abs contact-band"></div>
  <p class="abs contact-line">WANT TO CONTACT, <small>just click on the contact button at the right</small></p>
  <a class="abs btn-pink contact-btn">CONTACT ME</a>

  <p class="abs follow-text">To get the latest update of me and my works</p>
  <a class="abs follow-btn">FOLLOW ME</a>
  <div class="abs follow-icons" aria-label="Social media links"><span class="social-chip"></span><span class="social-chip"></span><span class="social-chip"></span><span class="social-chip"></span><span class="social-chip"></span></div>

  <footer class="abs footer">© 2015, All Rights Reserved.</footer>
</div>
</body>
</html>
```